Lumeva Botanics Natural baby skin and hair care

We need a look and feel for a line of baby care products. A lotion, Wash and baby oil. We already have an existing line of products and are now venturing into baby care. We want a natural look with "love, softness and a touch of earth and Africa'

Industry/Entity Type

Retail

Font styles to use
Script

Colors
fbed22
f78f20
9bcb3c

Requirements
Must have
• Natural elements
Should not have
• Red, Black abstract shapes

```html
<!DOCTYPE html>
<html lang="en">
<head>
<meta charset="utf-8">
<title>Lumeva Botanics Baby Lotion Label</title>
<link href="https://fonts.googleapis.com/css2?family=Oswald:wght@300;400;500&family=Pinyon+Script&display=swap" rel="stylesheet">
<style>
  :root {
    --bg: #eef3f2;
    --label-white: #ffffff;
    --label-shade: #f1f3f3;
    --orange: #f78f20;
    --orange-deep: #e8741a;
    --green: #9bcb3c;
    --green-bright: #8fd42a;
    --olive: #5a5a48;
    --frame: #d9dcd6;
    --skin-light: #f5d9c6;
    --skin-mid: #e7b79c;
  }
  * { margin: 0; padding: 0; box-sizing: border-box; }
  html, body { width: 920px; height: 1200px; overflow: hidden; background: var(--bg); }
  .canvas { position: relative; width: 920px; height: 1200px; }
  .label {
    position: absolute; left: 188px; top: 12px; width: 544px; height: 1176px;
    background: linear-gradient(90deg, var(--label-shade), var(--label-white) 30%, var(--label-white) 70%, var(--label-shade));
    overflow: hidden;
  }
  .brand-frame {
    position: absolute; left: 113px; top: 38px; width: 310px; height: 309px;
    border: 2px solid var(--frame);
    display: flex; align-items: center; justify-content: center;
  }
  .brand-name {
    font-family: "Oswald", sans-serif; font-weight: 300; font-size: 26px;
    letter-spacing: 5px; color: var(--olive); text-transform: uppercase;
    margin-top: 150px;
  }
  .headline { position: absolute; left: 0; top: 360px; width: 544px; height: 290px; }
  .headline text { font-family: "Oswald", sans-serif; font-weight: 400; }
  .band-green {
    position: absolute; left: 0; top: 732px; width: 544px; height: 156px;
    background: linear-gradient(90deg, var(--green-bright), var(--green));
  }
  .band-orange {
    position: absolute; left: 0; top: 888px; width: 544px; height: 288px;
    background: linear-gradient(180deg, var(--orange), var(--orange-deep));
  }
  .baby-photo {
    position: absolute; left: 58px; top: 673px; width: 180px; height: 238px;
    border-radius: 90px 90px 30px 30px;
    background: radial-gradient(circle at 50% 35%, var(--skin-light), var(--skin-mid));
  }
  .badge-natural {
    position: absolute; left: 224px; top: 690px; width: 93px; height: 89px;
    background: var(--orange); border: 3px solid var(--label-white);
    color: var(--label-white); text-align: center; font-family: "Oswald", sans-serif;
  }
  .badge-natural .all { display: block; font-size: 38px; font-weight: 400; line-height: 46px; margin-top: 2px; }
  .badge-natural .natural { display: block; font-size: 18px; font-weight: 500; line-height: 22px; }
  .tagline {
    position: absolute; left: 252px; top: 782px; width: 190px;
    font-family: "Pinyon Script", cursive; font-size: 31px; line-height: 30px;
    color: var(--label-white);
  }
  .tagline span { display: block; }
  .tagline span + span { padding-left: 6px; }
  .volume {
    position: absolute; left: 231px; top: 863px; width: 82px; height: 82px;
    border-radius: 50%; background: var(--orange);
    border: 4px solid var(--label-white); box-shadow: 0 0 0 3px var(--green);
    color: var(--label-white); font-family: "Oswald", sans-serif; font-size: 17px;
    line-height: 20px; text-align: center; padding-top: 16px;
  }
  .description {
    position: absolute; left: 100px; top: 944px; width: 344px;
    font-family: "Oswald", sans-serif; font-weight: 500; font-size: 18px;
    line-height: 29px; color: var(--label-white); text-align: center;
  }
</style>
</head>
<body>
<div class="canvas">
  <section class="label">
    <div class="brand-frame">
      <span class="brand-name">Lumeva Botanics</span>
    </div>

    <svg class="headline" viewBox="0 0 544 290" aria-label="Baby Lotion, Shea Butter and Honey">
      <text x="113" y="100" font-size="110" fill="#f78f20" textLength="313" lengthAdjust="spacingAndGlyphs">BABY LOTION</text>
      <text x="113" y="186" font-size="100" fill="#8fd42a" textLength="313" lengthAdjust="spacingAndGlyphs">SHEA BUTTER</text>
      <text x="167" y="274" font-size="100" fill="#8fd42a" textLength="202" lengthAdjust="spacingAndGlyphs">&amp; HONEY</text>
    </svg>

    <div class="band-green"></div>
    <div class="band-orange"></div>

    <div class="baby-photo" role="img" aria-label="Photo of a seated baby looking upward"></div>

    <div class="badge-natural">
      <span class="all">ALL</span>
      <span class="natural">NATURAL</span>
    </div>

    <p class="tagline"><span>Moisturising</span><span>&amp; Soothing</span></p>

    <div class="volume">250ml<br>(8oz.)</div>

    <p class="description">Harvested under the beautiful African Sun, Shea Butter, Honey, and Marula oil and Buttermilk are infused with precious essential oils and the soothing Aloe Vera to produce Lumeva Botanics deeply nourishing Baby Lotion.</p>
  </section>
</div>
</body>
</html>
```